Dane Morrow films- wedding and event films company website. DESKTOP AND MOBILE

We need a website for a high-end wedding and event film production company. Looking for a very modern and elegant design. my old website is www.danemorrowfilms.example

I like the "white/black/rose gold" color scheme of my logo.

really looking for a sleek modern design the breaths professional and artistic.

Target Market(s)

wedding and event films.

Industry/Entity Type

Film Production

Number of Pages Required

5+ page

Colors

Designer to choose colors to be used in the design.

Requirements
Must have
• website name will be www.danemorrowfilms.example
• tagline is "CINEMATIC STORIES ABOUT YOU"
• sections: HOME, CONTACT, ABOUT, FILMS, BLOG
• You can see my old website at danemorrowfilms.example
• Website about section:
• Dane Morrow Films was Established with the basis of truly cinematic and artistic films in mind. Dane and his team routinely travel the globe documenting weddings and events for high profile clients and discerning couples. Dane was born and raised in Maui Hawaii and has a unique approach to his films that embody the essence of a Hollywood film. Dane has spent the last 10 years traveling the world documenting corporate events and weddings with multiple Award winning production companies. In 2017 Dane decided to establish his own brand “Dane Morrow films” that will take everything he has learned with his past experiences and push it to the next level. Aside from his personal achievements, Dane is extremely passionate about his craft and always looks forward to handcrafting beautiful wedding/event films for his clients. The style of work is non-traditional and the day of filming is extremely unobtrusive (as we are looking for natural-candid/ raw emotions).
• If you are looking for the best price in town, we are probably not the best option, but if you’re looking for the best quality and peace of mind on your wedding day, then you’re in the right place. Dane Morrow Films is a boutique studio that only accepts a limited number of assignments per year. Inquire early to ensure availability.
• LINKS TO VIMEO VIDEOS THAT WILL BE IN THE "FILMS' SECTION.
• BRENT FILM TRAILER - https://clipvault.example/508114362
• BRENT FEATURE FILM - https://clipvault.example/617392048
• JUNE AND ROB'S WEDDING - https://clipvault.example/724958160
• DRONE DEMO REEL - https://clipvault.example/841576203
• WEDDING INDUSTRY EVENT PARTY - https://clipvault.example/962304817/a8d3e7b21c
• images that you can use on site are here: https://brigittolsenimages.proofbox.example/gallery/nora&felix/
• password is: meadow

```html
<!DOCTYPE html>
<html lang="en">
<head>
<meta charset="utf-8">
<title>Dane Morrow Films — Cinematic Stories About You</title>
<link href="https://fonts.googleapis.com/css2?family=Poppins:wght@300;400;500;600&display=swap" rel="stylesheet">
<style>
:root{
  --copper:#d68a4e;
  --copper-light:#e8a671;
  --copper-dark:#b9662c;
  --peach:#efb384;
  --brown:#b1612b;
  --ink:#222222;
  --text:#555555;
  --muted:#8a8a8a;
  --field:#f2f2f2;
  --field-line:#e3e3e3;
  --footer:#161616;
  --white:#ffffff;
}
*{box-sizing:border-box;margin:0;padding:0}
html,body{width:1200px;height:3586px;overflow:hidden}
body{position:relative;font-family:'Poppins',sans-serif;color:var(--text);background:var(--white)}
.abs{position:absolute}

/* header + hero */
.hero{left:0;top:0;width:1200px;height:686px;background:linear-gradient(100deg,#2a3340 0%,#3b4654 35%,#4a4f57 55%,#27303b 100%)}
.hero-shade{left:0;top:0;width:1200px;height:686px;background:linear-gradient(180deg,rgba(10,15,25,.35),rgba(10,15,25,.15) 50%,rgba(10,15,25,.55))}
.brand{left:112px;top:0;width:153px;height:110px;background:#111;display:flex;flex-direction:column;align-items:center;justify-content:center;gap:8px}
.brand-dot{width:18px;height:18px;border-radius:50%;background:var(--copper-light)}
.brand-name{color:var(--white);font-size:13px;font-weight:500;letter-spacing:1px;text-transform:uppercase;text-align:center;line-height:1.3}
.navbar{left:265px;top:72px;width:823px;height:38px;background:linear-gradient(90deg,var(--copper-dark),var(--copper-light));clip-path:polygon(0 0,100% 0,97.5% 50%,100% 100%,0 100%)}
.nav-link{top:72px;height:38px;line-height:38px;color:var(--white);font-size:13px;font-weight:500;text-transform:uppercase}
.social{top:84px;width:14px;height:14px;border-radius:50%;background:var(--white)}
.book{left:975px;top:19px;width:113px;height:36px;background:var(--copper);color:var(--white);font-size:13px;font-weight:500;text-align:center;line-height:36px}
.hero-title{left:0;top:330px;width:1200px;text-align:center;color:var(--white);font-size:54px;font-weight:300}
.hero-sub{left:280px;top:404px;width:640px;text-align:center;color:var(--white);font-size:17px;line-height:28px}
.dots{left:568px;top:632px;display:flex;gap:9px}
.dots span{width:10px;height:10px;border-radius:50%;background:rgba(255,255,255,.45)}
.dots span:first-child{background:var(--white)}

/* section heading */
.heading{left:0;width:1200px;text-align:center;color:var(--ink);font-size:36px;font-weight:400}
.divider{left:510px;width:180px;height:22px}

/* welcome */
.welcome-title{left:0;top:748px;width:1200px;text-align:center;color:var(--ink);font-size:33px;font-weight:300}
.welcome-title b{font-weight:300;color:var(--ink);text-transform:uppercase;letter-spacing:1px}
.about{left:112px;top:828px;width:622px;font-size:12px;line-height:21px;color:var(--text)}
.about p+p{margin-top:10px}
.read-more{left:112px;top:1083px;width:77px;height:33px;background:var(--copper);color:var(--white);font-size:10px;font-weight:600;text-align:center;line-height:33px;text-transform:uppercase}
.portrait-frame{left:779px;top:832px;width:309px;height:284px;background:#1b1b1b}
.portrait{left:806px;top:840px;width:255px;height:268px;background:linear-gradient(160deg,#d9d9d9,#8c8c8c 60%,#4c4c4c)}
.sprocket{width:10px;height:12px;background:#e8e8e8;border-radius:2px}

/* films */
.films{left:0;top:1188px;width:1200px;height:844px;background:linear-gradient(180deg,rgba(239,179,132,.92),rgba(233,168,118,.95)),var(--peach)}
.films .heading,.films-lead{color:var(--white)}
.films-lead{left:112px;top:1336px;width:976px;text-align:center;font-size:11px;line-height:20px;color:#fff6ee}
.player{left:112px;top:1403px;width:976px;height:413px;background:linear-gradient(180deg,#bfc6c9 0%,#9aa4a6 45%,#8c8a84 70%,#6f6c66 100%)}
.player-bar{left:112px;top:1776px;width:976px;height:40px;background:rgba(0,0,0,.55)}
.player-tools{left:1048px;top:1403px;width:40px;height:170px;background:rgba(0,0,0,.45)}
.thumb{top:1843px;width:217px;height:112px;background:#111;padding:6px}
.thumb-img{width:100%;height:100%;display:flex;align-items:center;justify-content:center}
.play{width:34px;height:24px;background:rgba(0,0,0,.6);border-radius:4px;display:flex;align-items:center;justify-content:center}

/* blog */
.card{top:2187px;width:309px}
.card-date{position:absolute;left:0;top:0;width:44px;height:41px;background:var(--copper);color:var(--white);text-align:center;font-size:15px;font-weight:600;line-height:22px;padding-top:2px}
.card-date small{display:block;font-size:9px;font-weight:400;line-height:12px;background:#fff;color:var(--copper);margin:0 4px}
.card-title{position:absolute;left:54px;top:2px;width:255px;font-size:13px;font-weight:500;line-height:19px;color:var(--ink)}
.card-img{position:absolute;left:0;top:62px;width:309px;height:146px}
.card-text{position:absolute;left:0;top:222px;width:309px;font-size:11px;line-height:19px;color:var(--muted)}

/* testimonial */
.quote-band{left:0;top:2550px;width:1200px;height:371px;background:linear-gradient(180deg,rgba(177,97,43,.93),rgba(170,90,38,.95)),#5a3a25}
.quote{left:150px;top:2686px;width:900px;color:var(--white);font-size:12px;line-height:22px;font-style:normal}
.quote-by{left:850px;top:2771px;width:200px;text-align:right;color:var(--white);font-size:13px}
.arrow{width:16px;height:20px}

/* contact */
.field{background:var(--field);border:1px solid var(--field-line);font-size:11px;color:#a9a9a9;padding:0 14px;line-height:42px}
.send{left:535px;top:3355px;width:129px;height:34px;background:var(--copper);color:var(--white);font-size:10px;font-weight:600;text-align:center;line-height:34px;text-transform:uppercase}

/* footer */
.footer{left:0;top:3449px;width:1200px;height:137px;background:var(--footer)}
.foot-link{top:3490px;color:var(--white);font-size:11px}
.foot-rule{left:470px;top:3513px;width:260px;height:1px;background:#333}
.copyright{left:0;top:3522px;width:1200px;text-align:center;color:#bdbdbd;font-size:11px}
</style>
</head>
<body>

<!-- header / hero -->
<div class="abs hero" role="img" aria-label="Evening photograph of a bride and groom embracing by the sea"></div>
<div class="abs hero-shade"></div>
<div class="abs brand"><span class="brand-dot"></span><span class="brand-name">Dane Morrow<br>Films</span></div>
<div class="abs navbar"></div>
<span class="abs nav-link" style="left:311px">Home</span>
<span class="abs nav-link" style="left:433px">About</span>
<span class="abs nav-link" style="left:564px">Films</span>
<span class="abs nav-link" style="left:686px">Blog</span>
<span class="abs nav-link" style="left:808px">Contact</span>
<span class="abs social" style="left:944px"></span>
<span class="abs social" style="left:975px"></span>
<span class="abs social" style="left:1006px"></span>
<span class="abs social" style="left:1037px"></span>
<div class="abs book">BOOK NOW</div>
<h1 class="abs hero-title">Cinematic Stories About You</h1>
<p class="abs hero-sub">Dane Morrow Films is a boutique studio that only accepts a limited number of assignments per year. Inquire early to ensure availability</p>
<div class="abs dots"><span></span><span></span><span></span><span></span></div>

<!-- welcome -->
<h2 class="abs welcome-title">Welcome to <b>Dane Morrow Films</b></h2>
<div class="abs about">
  <p>Dane Morrow Films was Established with the basis of truly cinematic and artistic films in mind. Dane and his team routinely travel the globe documenting weddings and events for high profile clients and discerning couples. Dane was born and raised in Maui Hawaii and has a unique approach to his films that embody the essence of a Hollywood film. Dane has spent the last 10 years traveling the world documenting corporate events and weddings with multiple Award winning production companies.</p>
  <p>In 2017 Dane decided to establish his own brand "Dane Morrow films" that will take everything he has learned with his past experiences and push it to the next level. Aside from his personal achievements, Dane is extremely passionate about his craft and always looks forward to handcrafting beautiful wedding/event films for his clients. The style of work is non-traditional and the day</p>
</div>
<div class="abs read-more">Read More</div>
<div class="abs portrait-frame"></div>
<div class="abs portrait" role="img" aria-label="Black and white portrait of the filmmaker"></div>
<div class="abs" style="left:785px;top:846px;display:flex;flex-direction:column;gap:12px">
  <span class="sprocket"></span><span class="sprocket"></span><span class="sprocket"></span><span class="sprocket"></span><span class="sprocket"></span><span class="sprocket"></span><span class="sprocket"></span><span class="sprocket"></span><span class="sprocket"></span><span class="sprocket"></span><span class="sprocket"></span>
</div>
<div class="abs" style="left:1068px;top:846px;display:flex;flex-direction:column;gap:12px">
  <span class="sprocket"></span><span class="sprocket"></span><span class="sprocket"></span><span class="sprocket"></span><span class="sprocket"></span><span class="sprocket"></span><span class="sprocket"></span><span class="sprocket"></span><span class="sprocket"></span><span class="sprocket"></span><span class="sprocket"></span>
</div>

<!-- films -->
<section class="abs films" role="img" aria-label="Soft wedding reception photograph behind a peach overlay"></section>
<h2 class="abs heading" style="top:1238px;color:#fff">Films</h2>
<svg class="abs divider" style="top:1296px" viewBox="0 0 180 22"><line x1="0" y1="11" x2="72" y2="11" stroke="#fff" stroke-width="1.5"/><circle cx="90" cy="11" r="6" fill="#fff"/><line x1="108" y1="11" x2="180" y2="11" stroke="#fff" stroke-width="1.5"/></svg>
<p class="abs films-lead">Lorem ipsum dolor sit amet, consectetuer adipiscing elit, sed diam nonummy nibh euismod tincidunt ut laoreet dolore magna aliquam erat volutpat. Ut wisi enim ad minim veniam, quis nostrud exerci tation ullamcorper suscipit lobortis nisl ut aliquip.</p>
<div class="abs player" role="img" aria-label="Video still of a couple on a rocky coastline with a lighthouse"></div>
<div class="abs player-tools"></div>
<svg class="abs" style="left:1058px;top:1413px" width="20" height="150" viewBox="0 0 20 150" fill="none" stroke="#fff" stroke-width="2">
  <path d="M10 16 L3 9 a4 4 0 0 1 7-4 a4 4 0 0 1 7 4 Z" fill="#fff"/>
  <circle cx="10" cy="46" r="7"/><path d="M10 42v4l3 2"/>
  <path d="M3 80 L10 76 L17 80 L10 84 Z M3 86 L10 90 L17 86"/>
  <path d="M3 118 L17 111 L12 125 L10 119 Z" fill="#fff"/>
</svg>
<div class="abs player-bar"></div>
<svg class="abs" style="left:126px;top:1786px" width="950" height="20" viewBox="0 0 950 20">
  <path d="M4 3 L16 10 L4 17 Z" fill="#fff"/>
  <rect x="32" y="3" width="40" height="14" fill="#222"/>
  <text x="52" y="14" fill="#fff" font-size="9" text-anchor="middle" font-family="Poppins,sans-serif">05:21</text>
  <rect x="80" y="8" width="760" height="4" fill="rgba(255,255,255,.35)"/>
  <rect x="856" y="12" width="3" height="5" fill="#4fc3f7"/><rect x="861" y="9" width="3" height="8" fill="#4fc3f7"/><rect x="866" y="6" width="3" height="11" fill="#4fc3f7"/>
  <circle cx="905" cy="10" r="5" fill="none" stroke="#fff" stroke-width="2"/>
  <path d="M925 4h5M925 4v5M940 4h-5M940 4v5M925 16h5M925 16v-5M940 16h-5M940 16v-5" stroke="#fff" stroke-width="2"/>
</svg>
<svg class="abs arrow" style="left:98px;top:1890px" viewBox="0 0 16 20"><path d="M12 2 L4 10 L12 18" fill="none" stroke="#333" stroke-width="3"/></svg>
<svg class="abs arrow" style="left:1086px;top:1890px" viewBox="0 0 16 20"><path d="M4 2 L12 10 L4 18" fill="none" stroke="#333" stroke-width="3"/></svg>
<div class="abs thumb" style="left:127px"><div class="thumb-img" role="img" aria-label="Film thumbnail of a coastal wedding" style="background:linear-gradient(180deg,#b9c2c4,#7c807c)"><span class="play"><svg width="12" height="12"><path d="M2 1 L11 6 L2 11Z" fill="#fff"/></svg></span></div></div>
<div class="abs thumb" style="left:370px"><div class="thumb-img" role="img" aria-label="Film thumbnail of a waterside ceremony" style="background:linear-gradient(180deg,#aeb9c0,#8d8273)"><span class="play"><svg width="12" height="12"><path d="M2 1 L11 6 L2 11Z" fill="#fff"/></svg></span></div></div>
<div class="abs thumb" style="left:612px"><div class="thumb-img" role="img" aria-label="Film thumbnail of a couple at sunset" style="background:linear-gradient(180deg,#e0894a,#3a2a25)"><span class="play"><svg width="12" height="12"><path d="M2 1 L11 6 L2 11Z" fill="#fff"/></svg></span></div></div>
<div class="abs thumb" style="left:856px"><div class="thumb-img" role="img" aria-label="Film thumbnail of a mountain lake from a drone" style="background:linear-gradient(180deg,#8fb1c4,#3f6b5c)"><span class="play"><svg width="12" height="12"><path d="M2 1 L11 6 L2 11Z" fill="#fff"/></svg></span></div></div>

<!-- blog -->
<h2 class="abs heading" style="top:2078px">Latest Blog</h2>
<svg class="abs divider" style="top:2140px" viewBox="0 0 180 22"><line x1="0" y1="11" x2="72" y2="11" stroke="#e2b08a" stroke-width="1.5"/><circle cx="90" cy="11" r="6" fill="var(--copper)"/><line x1="108" y1="11" x2="180" y2="11" stroke="#e2b08a" stroke-width="1.5"/></svg>
<article class="abs card" style="left:112px">
  <div class="card-date">10<small>Dec</small></div>
  <h3 class="card-title">Nonummy nibh euismod tincidunt ut laoreet dolore magna</h3>
  <div class="card-img" role="img" aria-label="Party photograph of a performer pouring champagne" style="background:linear-gradient(135deg,#3b1e3a,#8a3d4a 50%,#d1a070)"></div>
  <p class="card-text">Sed diam nonummy nibh euismod tincidunt ut laoreet dolore magna aliquam erat volutpat. Ut wisi enim ad minim veniam, quis nostrud exerci tation ullamcorper suscipit lobortis nisl ut aliquip...</p>
</article>
<article class="abs card" style="left:445px">
  <div class="card-date">10<small>Dec</small></div>
  <h3 class="card-title">Nonummy nibh euismod tincidunt ut laoreet dolore magna</h3>
  <div class="card-img" role="img" aria-label="Photograph of a bride's gown with a long train" style="background:radial-gradient(circle at 50% 60%,#d8d2c8,#4a4440 70%)"></div>
  <p class="card-text">Sed diam nonummy nibh euismod tincidunt ut laoreet dolore magna aliquam erat volutpat. Ut wisi enim ad minim veniam, quis nostrud exerci tation ullamcorper suscipit lobortis nisl ut aliquip...</p>
</article>
<article class="abs card" style="left:779px">
  <div class="card-date">10<small>Dec</small></div>
  <h3 class="card-title">Nonummy nibh euismod tincidunt ut laoreet dolore magna</h3>
  <div class="card-img" role="img" aria-label="Photograph of guests dancing at a wedding reception" style="background:linear-gradient(135deg,#6b5fa6,#c7a3d6 50%,#3d2f5a)"></div>
  <p class="card-text">Sed diam nonummy nibh euismod tincidunt ut laoreet dolore magna aliquam erat volutpat. Ut wisi enim ad minim veniam, quis nostrud exerci tation ullamcorper suscipit lobortis nisl ut aliquip...</p>
</article>

<!-- testimonial -->
<section class="abs quote-band" role="img" aria-label="Group photograph of wedding guests behind a copper overlay"></section>
<svg class="abs arrow" style="left:98px;top:2717px" viewBox="0 0 16 20"><path d="M12 2 L4 10 L12 18" fill="none" stroke="#fff" stroke-width="3"/></svg>
<svg class="abs arrow" style="left:1086px;top:2717px" viewBox="0 0 16 20"><path d="M4 2 L12 10 L4 18" fill="none" stroke="#fff" stroke-width="3"/></svg>
<blockquote class="abs quote">"Lorem ipsum dolor sit amet, consectetuer adipiscing elit, sed diam nonummy nibh euismod tincidunt ut laoreet dolore magna aliquam erat volutpat. Ut wisi enim ad minim veniam, quis nostrud exerci tation ullamcorper suscipit lobortis nisl ut aliquip ex ea commodo consequat. Duis autem vel illamcorper suscipit lobortis nisl ut aliquip ex ea commodo consequat"</blockquote>
<p class="abs quote-by">~ Ipsum Dolor Name</p>

<!-- contact -->
<h2 class="abs heading" style="top:2955px">Contact Us</h2>
<svg class="abs divider" style="top:3017px" viewBox="0 0 180 22"><line x1="0" y1="11" x2="72" y2="11" stroke="#e2b08a" stroke-width="1.5"/><circle cx="90" cy="11" r="6" fill="var(--copper)"/><line x1="108" y1="11" x2="180" y2="11" stroke="#e2b08a" stroke-width="1.5"/></svg>
<div class="abs field" style="left:158px;top:3085px;width:430px;height:44px">First Name</div>
<div class="abs field" style="left:605px;top:3085px;width:432px;height:44px">Last Name</div>
<div class="abs field" style="left:158px;top:3145px;width:430px;height:44px">Email</div>
<div class="abs field" style="left:605px;top:3145px;width:432px;height:44px">Contact</div>
<div class="abs field" style="left:158px;top:3207px;width:879px;height:103px">Text Message</div>
<div class="abs send">Send Message</div>

<!-- footer -->
<footer class="abs footer"></footer>
<span class="abs foot-link" style="left:343px">Home</span>
<span class="abs foot-link" style="left:470px">About</span>
<span class="abs foot-link" style="left:600px">Films</span>
<span class="abs foot-link" style="left:720px">Blog</span>
<span class="abs foot-link" style="left:843px">Contact</span>
<div class="abs foot-rule"></div>
<p class="abs copyright">© All rights Reserved 2017.</p>

</body>
</html>
```